Business Card, A4 Letter Head and DL Envelope for Brandolux

We are looking for a design for our Business Card, A4 Letter Head and DL Envelope.

Brandolux is a distributor of promotional products. We specialize in a range of branded promotional products, these include pens, polo shirts, key rings, drink bottles, uniforms and bags to name a few. We are experts in marketing and assist companies in choosing the right promotional product for their needs. We will predominately be an online business where customers visit our website and browse our range of promotional products and branding options.

Our colours are black, red, white and grey.

Files must be supplied in eps, pdf and ai format.

Please display the following information:
Dorian Pell
Account Manager
Suite xxx, 214 Harwick Lane Melbourne, Victoria 3000
Phone +61 3 5550 1842
Mobile +61 455 501 736
sales@brandolux.example
www.brandolux.example

```html
<!DOCTYPE html>
<html lang="en">
<head>
<meta charset="utf-8">
<title>Brandolux Business Card</title>
<link rel="stylesheet" href="https://fonts.googleapis.com/css2?family=Open+Sans:wght@400;600;700;800&display=swap">
<style>
  :root {
    --bg: #ecebe8;
    --red: #d4161d;
    --red-deep: #8e0a10;
    --red-bright: #ee2128;
    --white: #ffffff;
    --grey: #9a9a9a;
    --grey-light: #d8d8d8;
    --grey-dark: #5c5c5c;
    --black: #161616;
  }
  * { margin: 0; padding: 0; box-sizing: border-box; }
  html, body { width: 1200px; height: 1024px; overflow: hidden; }
  body {
    background: var(--bg);
    font-family: "Open Sans", Arial, sans-serif;
    position: relative;
  }
  .card {
    position: absolute;
    left: 180px;
    width: 840px;
    height: 480px;
    border-radius: 26px;
    overflow: hidden;
    box-shadow: 0 10px 28px rgba(0,0,0,0.22);
  }
  .card--front { top: 24px; background: var(--white); }
  .card--back {
    top: 524px;
    background: radial-gradient(ellipse at 45% 50%, var(--red-bright) 0%, var(--red) 45%, var(--red-deep) 100%);
  }
  .front-bands { position: absolute; inset: 0; width: 100%; height: 100%; }

  .brand {
    position: absolute;
    display: flex;
    align-items: center;
    gap: 16px;
  }
  .brand__dot { border-radius: 50%; }
  .brand__name { font-weight: 800; letter-spacing: 1px; text-transform: uppercase; }

  .card--front .brand { left: 58px; top: 206px; }
  .card--front .brand__dot { width: 58px; height: 58px; background: var(--red); }
  .card--front .brand__name { font-size: 46px; color: var(--grey-dark); }

  .holder { position: absolute; right: 60px; top: 46px; text-align: right; }
  .holder__name { font-size: 30px; font-weight: 800; color: var(--red); text-transform: uppercase; letter-spacing: 0.5px; line-height: 1.1; }
  .holder__role { font-size: 17px; color: var(--grey-dark); font-weight: 600; }

  .contacts {
    position: absolute; left: 560px; top: 206px;
    list-style: none; color: var(--white);
    font-size: 17px; line-height: 1.55;
  }
  .address {
    position: absolute; left: 420px; top: 368px;
    color: var(--white); font-size: 17px; line-height: 1.5;
    font-style: normal;
  }

  .card--back .brand { left: 450px; top: 332px; flex-direction: column; align-items: flex-start; gap: 4px; }
  .card--back .brand__name { font-size: 50px; color: var(--white); }
  .card--back .brand__url { font-size: 17px; color: var(--white); }
</style>
</head>
<body>

<section class="card card--front" aria-label="Business card front">
  <svg class="front-bands" viewBox="0 0 840 480" preserveAspectRatio="none" aria-hidden="true">
    <defs>
      <linearGradient id="redFill" x1="0" y1="0" x2="1" y2="1">
        <stop offset="0" stop-color="var(--red-bright)"/>
        <stop offset="1" stop-color="var(--red-deep)"/>
      </linearGradient>
      <linearGradient id="greyFill" x1="0" y1="0" x2="1" y2="0">
        <stop offset="0" stop-color="var(--grey-light)"/>
        <stop offset="0.5" stop-color="var(--grey)"/>
        <stop offset="1" stop-color="var(--grey-light)"/>
      </linearGradient>
    </defs>
    <path class="band band--grey" d="M840,112 C640,112 520,170 430,300 C380,380 340,450 250,480 L840,480 Z" fill="url(#greyFill)"/>
    <path class="band band--black" d="M840,136 C650,136 540,190 455,310 C405,390 370,455 300,480 L840,480 Z" fill="var(--black)"/>
    <path class="band band--red" d="M840,144 C655,144 548,198 464,316 C414,394 380,458 318,480 L840,480 Z" fill="url(#redFill)"/>
  </svg>

  <div class="brand">
    <span class="brand__dot"></span>
    <span class="brand__name">Brandolux</span>
  </div>

  <div class="holder">
    <p class="holder__name">Dorian Pell</p>
    <p class="holder__role">Account Manager</p>
  </div>

  <ul class="contacts">
    <li>P : +61 3 5550 1842</li>
    <li>M : +61 455 501 736</li>
    <li>E : sales@brandolux.example</li>
    <li>W : www.brandolux.example</li>
  </ul>

  <address class="address">
    Suite xxx, 214 Harwick Lane<br>
    Melbourne, Victoria 3000<br>
    ABN : 00 000 000 000
  </address>
</section>

<section class="card card--back" aria-label="Business card back">
  <div class="brand">
    <span class="brand__name">Brandolux</span>
    <span class="brand__url">www.brandolux.example</span>
  </div>
</section>

</body>
</html>
```